Business Card Design Project

Name: Kunle O. Edet
Designation: Partner
Address: QRM Building, 14 Harmony Close, P.O. Box 58314, Victoria Island Lagos, Nigeria
Tel: +234 1 7395162
mobile: +234 1 7061527394
Email: koedet@larkmoorassociates.com
website www.larkmoorassociates.com

```html
<!DOCTYPE html>
<html lang="en">
<head>
<meta charset="utf-8">
<title>Larkmoor Associates – Business Card</title>
<link href="https://fonts.googleapis.com/css2?family=Oswald:wght@400;500&family=Alegreya+Sans:wght@400;500;700&display=swap" rel="stylesheet">
<style>
  :root {
    --backdrop: #1c1c1e;
    --card-black: #0b0b0c;
    --maroon-top: #2e0619;
    --maroon-bottom: #650d3b;
    --silver-light: #e6e8ec;
    --silver-dark: #6e7078;
    --ink-light: #e2e8f3;
    --ink-white: #ffffff;
    --brand-grey: #c9ccd3;
  }
  html, body {
    margin: 0;
    padding: 0;
    width: 922px;
    height: 1200px;
    overflow: hidden;
    background: var(--backdrop);
  }
  .canvas {
    position: relative;
    width: 922px;
    height: 1200px;
  }
  .card {
    position: absolute;
    left: 71px;
    top: 375px;
    width: 780px;
    height: 450px;
    background: var(--card-black);
    overflow: hidden;
    box-shadow: 0 10px 30px rgba(0,0,0,0.5);
  }
  .brand {
    position: absolute;
    left: 70px;
    top: 175px;
    display: flex;
    align-items: center;
    gap: 16px;
    font-family: "Alegreya Sans", sans-serif;
    font-weight: 500;
    color: var(--brand-grey);
  }
  .brand-mark {
    width: 18px;
    height: 18px;
    border-radius: 50%;
    background: var(--brand-grey);
  }
  .brand-name {
    font-size: 44px;
    line-height: 1;
  }
  .brand-sub {
    display: block;
    font-size: 22px;
    text-align: right;
    margin-top: 4px;
  }
  .info-panel {
    position: absolute;
    left: 345px;
    top: 0;
    right: 0;
    bottom: 0;
    border-left: 10px solid var(--silver-light);
    border-radius: 54px 0 0 54px;
    background: linear-gradient(160deg, var(--maroon-top) 0%, #4a0a2b 50%, var(--maroon-bottom) 100%);
    box-shadow: -4px 0 0 var(--silver-dark);
  }
  .holder {
    position: absolute;
    right: 40px;
    top: 42px;
    text-align: right;
  }
  .holder-name {
    font-family: "Oswald", sans-serif;
    font-weight: 500;
    font-size: 44px;
    line-height: 1;
    color: var(--ink-light);
    letter-spacing: 0.5px;
    margin: 0;
  }
  .holder-role {
    font-family: "Oswald", sans-serif;
    font-weight: 500;
    font-size: 22px;
    color: var(--ink-white);
    margin: 12px 0 0;
  }
  .address {
    position: absolute;
    left: 30px;
    right: 30px;
    top: 175px;
    font-family: "Alegreya Sans", sans-serif;
    font-size: 20px;
    line-height: 33px;
    color: var(--ink-white);
    text-align: center;
  }
  .address .home-icon {
    width: 22px;
    height: 20px;
    vertical-align: -3px;
    margin-right: 4px;
  }
  .contacts {
    position: absolute;
    left: 40px;
    top: 318px;
    font-family: "Alegreya Sans", sans-serif;
    font-size: 16px;
    line-height: 30px;
    color: var(--ink-white);
    list-style: none;
    margin: 0;
    padding: 0;
  }
</style>
</head>
<body>
<main class="canvas">
  <section class="card">
    <div class="brand">
      <span class="brand-mark"></span>
      <div>
        <span class="brand-name">Larkmoor</span>
        <span class="brand-sub">Associates</span>
      </div>
    </div>

    <div class="info-panel">
      <div class="holder">
        <h1 class="holder-name">Kunle O. Edet</h1>
        <p class="holder-role">Partner</p>
      </div>

      <p class="address">
        <svg class="home-icon" viewBox="0 0 22 20" aria-hidden="true">
          <path d="M11 1 L1 10 H4 V19 H9 V13 H13 V19 H18 V10 H21 Z" fill="#1a0a12"/>
        </svg>QRM Building, 14 Harmony Close,<br>
        P.O. Box 58314,<br>
        Victoria Island Lagos, Nigeria
      </p>

      <ul class="contacts">
        <li>E:- koedet@larkmoorassociates.com</li>
        <li>W:- www.larkmoorassociates.com</li>
        <li>T:- +23417395162</li>
      </ul>
    </div>
  </section>
</main>
</body>
</html>
```